Plakat-Design für Escaperoom
Zielgruppe
Ich benötige ein Plakatdesign für unseren Escaperoom. Die zielgruppe sind Personen im Alter von 18 -35 Jahre
Aufgabenstellung
Ich habe jetzt noch ein Bilder hinzugefügt, mit denen ich bisher Werbung für den Escaperoom gemacht habe, die machen es vielleicht etwa deutlicher und auch unser Logo in den normalen Farben und in grau. Das Bild vom Escaperoom soll nicht unbedingt verwendet werden. Das Wappen ist selbstdesigned, welches in den Geschichten auch eine Rolle spielt. Die Geschichte im Escaperoom dreht sich um eine Weinbruderschaft, die von der Bevölkerung auch Moseltal-Bande genannt wird. Der Raum ist als Weinstube eingerichtet.

```html
<!DOCTYPE html>
<html lang="de">
<head>
<meta charset="utf-8">
<title>Escaperoom – Pfuscht der Moseltal-Bande ins Handwerk!</title>
<link href="https://fonts.googleapis.com/css2?family=Bebas+Neue&display=swap" rel="stylesheet">
<style>
  :root {
    --night: #000000;
    --light: #ffffff;
    --wine-red: #e31b23;
    --ink: #000000;
  }
  html, body {
    margin: 0;
    padding: 0;
    overflow: hidden;
    background: var(--night);
  }
  .poster {
    position: relative;
    width: 848px;
    height: 1200px;
    overflow: hidden;
    background: var(--night);
  }
  .poster-art {
    position: absolute;
    inset: 0;
    display: block;
  }
  .bottle-area { fill: var(--wine-red); }
  .headline,
  .slogan,
  .brand-name {
    font-family: "Bebas Neue", "Oswald", sans-serif;
    text-anchor: middle;
  }
  .headline { fill: var(--wine-red); font-size: 92px; }
  .slogan { fill: var(--ink); font-size: 92px; }
  .slogan--region { font-size: 86px; }
  .slogan .accent { fill: var(--wine-red); }
  .brand-name { fill: var(--wine-red); font-size: 27px; }
</style>
</head>
<body>
  <main class="poster">
    <svg class="poster-art" viewBox="0 0 848 1200" width="848" height="1200" xmlns="http://www.w3.org/2000/svg">
      <defs>
        <linearGradient id="doorway-glow" x1="0" y1="0" x2="0" y2="1">
          <stop offset="0" stop-color="#000000"/>
          <stop offset="0.45" stop-color="#ffffff"/>
          <stop offset="1" stop-color="#ffffff"/>
        </linearGradient>
      </defs>

      <text class="headline" x="424" y="137">ESCAPEROOM</text>

      <rect class="doorway-area" x="0" y="200" width="848" height="1000" fill="url(#doorway-glow)"
        role="img" aria-label="Illustration: offene Tür im Dunkeln, aus der ein Lichtkegel auf den Boden fällt"/>

      <rect class="bottle-area" x="426" y="297" width="70" height="250" rx="8"
        role="img" aria-label="Rote Weinflasche als Silhouette in der offenen Tür"/>

      <text class="slogan" x="437" y="748">PFUSCHT</text>
      <text class="slogan" x="437" y="849">DER</text>
      <text class="slogan slogan--region" x="437" y="947"><tspan class="accent">MOSELTAL</tspan>-BANDE</text>
      <text class="slogan" x="436" y="1046">INS HANDWERK!</text>

      <text class="brand-name" x="435" y="1118">SPASS AM FLUSS</text>
      <text class="brand-name" x="435" y="1146">EVENTS</text>
    </svg>
  </main>
</body>
</html>
```